International Film making Business needs the 5 Logos provided made into a POSTER Format

Design Task:
CREATE A POSTER DESIGN USING THE 5 LOGOS PROVIDED. The GLAD SKY VISTA LOGO should stand out from the others by being in the middle with the other 4 logos connected to it somehow.

The 5 Businesses already has their 5 Logos, all similar in design to each other.

GLAD SKY VISTA is the Main Logo that encompasses the other 4 Logos. So it must stand out more and it is like the Overall Business entity that incorporates the other 4 Logos.

What is required is that by using the 5 Logo designs provided, create a cool graphic artwork that somehow incorporates ALL of the 5 Logos - But having the GLAD SKY VISTA Logo at the forefront/most important/standing out the most.
- GLAD SKY VISTA will probably be bigger than the others
- and could be changed into 3D.

I have attached all 5 logos and a hand drawn example of how the GLAD SKY VISTAS could stand out from the rest.

THE DESIGNS OF THE LOGOS SHOULD NOT BE CHANGED (except the GLADSKYVISTA which can be 3D)

Please do not be restricted with the sample idea. Creativity is encouraged

DIMENSION: 3000 mm x 6000 mm
high resolution graphic

Logo Text

glad sky , glad sky reels, glad sky tales, glad sky groovy, GLAD SKY VISTAS

Requirements
Must have
• USE THE 5 LOGOS PROVIDED ONLY - Only GLAD SKY VISTA can be changed into 3D only
Nice to have
• Eye catching design, showing the Glad Sky Vista as the most powerful Logo that has the other 4 as subordinate companies
Should not have
• ANY CHANGE IN THE 5 LOGO DESIGNS (EXcept 3D for Glad Sky Vistas)

```html
<!DOCTYPE html>
<html lang="en">
<head>
<meta charset="utf-8">
<title>Glad Sky Vistas</title>
<link rel="stylesheet" href="https://fonts.googleapis.com/css2?family=Cinzel:wght@600&family=Montserrat:wght@500&display=swap">
<style>
  :root {
    --space-deep: #05040c;
    --space-violet: #4a2a7a;
    --space-magenta: #b0479a;
    --space-glow: #d9d4ff;
    --star-blue: #7fb8ff;
    --gold-light: #f4d27a;
    --gold-mid: #c8952e;
    --gold-frame: #8a6a2a;
    --oval-white: #ffffff;
    --brand-blue: #2a8fd6;
    --brand-tales: #b03aa8;
    --brand-reels: #2e2e2e;
    --brand-groovy: #6a2a9a;
    --url-white: #f2f2f2;
  }
  html, body {
    margin: 0;
    padding: 0;
    overflow: hidden;
    background: var(--space-deep);
  }
  .poster {
    position: relative;
    width: 1200px;
    height: 600px;
    overflow: hidden;
    font-family: "Cinzel", Georgia, serif;
  }
  .space-scene {
    position: absolute;
    inset: 0;
    background:
      radial-gradient(circle 40px at 80px 345px, var(--star-blue) 0%, rgba(127,184,255,0) 100%),
      radial-gradient(circle 40px at 1115px 310px, var(--star-blue) 0%, rgba(127,184,255,0) 100%),
      radial-gradient(circle 36px at 650px 110px, var(--star-blue) 0%, rgba(127,184,255,0) 100%),
      radial-gradient(ellipse 240px 180px at 500px 270px, var(--space-glow) 0%, rgba(217,212,255,0) 70%),
      radial-gradient(ellipse 400px 290px at 580px 330px, var(--space-magenta) 0%, rgba(176,71,154,0) 70%),
      radial-gradient(ellipse 620px 420px at 600px 300px, var(--space-violet) 0%, rgba(74,42,122,0) 75%),
      var(--space-deep);
  }
  .artwork {
    position: absolute;
    inset: 0;
  }
  .sub-brand {
    position: absolute;
    width: 308px;
    height: 164px;
    display: flex;
    align-items: center;
    justify-content: center;
    gap: 12px;
  }
  .sub-brand .mark {
    width: 40px;
    height: 40px;
    border-radius: 50%;
    flex: none;
  }
  .sub-brand .name {
    font-weight: 600;
    font-size: 30px;
    line-height: 1.1;
    letter-spacing: 1px;
  }
  .brand-glad-sky { left: 67px; top: 53px; }
  .brand-glad-sky .mark { background: var(--brand-blue); }
  .brand-glad-sky .name { color: var(--brand-blue); }
  .brand-tales { left: 818px; top: 62px; }
  .brand-tales .mark { background: var(--brand-tales); }
  .brand-tales .name { color: var(--brand-tales); }
  .brand-reels { left: 67px; top: 389px; }
  .brand-reels .mark { background: var(--brand-reels); }
  .brand-reels .name { color: var(--brand-reels); }
  .brand-groovy { left: 818px; top: 399px; }
  .brand-groovy .mark { background: var(--brand-groovy); }
  .brand-groovy .name { color: var(--brand-groovy); }
  .main-brand {
    position: absolute;
    left: 345px;
    top: 215px;
    width: 480px;
    display: flex;
    align-items: center;
    gap: 22px;
  }
  .main-brand .mark {
    width: 120px;
    height: 120px;
    border-radius: 50%;
    background: var(--gold-mid);
    flex: none;
  }
  .main-brand .text {
    display: flex;
    flex-direction: column;
  }
  .main-brand .name {
    font-weight: 600;
    font-size: 48px;
    line-height: 1.05;
    letter-spacing: 3px;
    color: var(--gold-light);
    margin: 0;
  }
  .main-brand .url {
    font-family: "Montserrat", Arial, sans-serif;
    font-weight: 500;
    font-size: 19px;
    color: var(--url-white);
    letter-spacing: 0.5px;
    margin-top: 6px;
  }
</style>
</head>
<body>
<main class="poster">
  <div class="space-scene" role="img" aria-label="Deep space backdrop with a violet and pink nebula and bright blue star flares"></div>

  <svg class="artwork" width="1200" height="600" viewBox="0 0 1200 600" aria-hidden="true">
    <rect class="frame" x="40" y="58" width="1120" height="505" fill="none" stroke="var(--gold-frame)" stroke-width="1.5"/>
    <ellipse class="orbit" cx="596" cy="308" rx="440" ry="260" fill="none" stroke="var(--gold-mid)" stroke-width="6"/>
    <g class="oval-rings" fill="none" stroke="var(--gold-light)" stroke-width="5">
      <ellipse cx="221" cy="135" rx="168" ry="96"/>
      <ellipse cx="972" cy="144" rx="168" ry="96"/>
      <ellipse cx="221" cy="471" rx="168" ry="96"/>
      <ellipse cx="972" cy="481" rx="168" ry="96"/>
    </g>
    <g class="ovals" fill="var(--oval-white)">
      <ellipse cx="221" cy="135" rx="154" ry="82"/>
      <ellipse cx="972" cy="144" rx="154" ry="82"/>
      <ellipse cx="221" cy="471" rx="154" ry="82"/>
      <ellipse cx="972" cy="481" rx="154" ry="82"/>
    </g>
  </svg>

  <div class="sub-brand brand-glad-sky">
    <span class="mark"></span>
    <span class="name">GLAD<br>SKY</span>
  </div>
  <div class="sub-brand brand-tales">
    <span class="mark"></span>
    <span class="name">GLAD SKY<br>TALES</span>
  </div>
  <div class="sub-brand brand-reels">
    <span class="mark"></span>
    <span class="name">GLAD SKY<br>REELS</span>
  </div>
  <div class="sub-brand brand-groovy">
    <span class="mark"></span>
    <span class="name">GLAD SKY<br>GROOVY</span>
  </div>

  <div class="main-brand">
    <span class="mark"></span>
    <div class="text">
      <h1 class="name">GLAD SKY<br>VISTAS</h1>
      <span class="url">gladskyvistas.com.au</span>
    </div>
  </div>
</main>
</body>
</html>
```